Business Card Design Project : Tidewell Press

In preparation for market launch, Whistler's Tidewell Press require the development of a business card. Tidewell Press is a Community online publishing web portal. We provide the the city of Whistler located in B.C. (Canada) business directories, News, Classified ads, News, Events and blogs etc.

The main focus of the brand is to help local businesses to corporate with their online advertisement and marketing. Meeting our clients face to face is a must (B2B).

Target Market(s)

The target market is B2B customers. Business Owners to Marketing, advertising Managers

Industry/Entity Type

Business

Requirements
Must have
• - The business card will be two sided.
the BACK side will have our logo which consist of (icon, url,slogan) submited. The logo will be middle and centred.

The FRONT side should have company details:

Company Legal Name: FERNDALE TIDEWELL PRESS

Owen Marsk
Director of Sales & Marketing

www.ferndaletidewell.biz
owen@ferndaletidewell.biz

Phone: 555 014 3826
#2817 - 562 E. Harlow Ave.
Vancouver, B.C. K7P2R4 Canada
Nice to have
• - For the "FRONT" side of our business card. You can separate or re-arrange with our logo components (icon, logo,slogan). It does not have to be together.

Also our company legal name is rather long so arrange or organize the name in a way to make it shorter. Your experience and creativity will have to come in play.
Should not have
• should not have other colors beside logo color and black text (2 colors). Also nothing Three dimensional

```html
<!DOCTYPE html>
<html lang="en">
<head>
<meta charset="utf-8">
<title>Ferndale Tidewell Press — Business Card</title>
<link rel="stylesheet" href="https://fonts.googleapis.com/css2?family=Open+Sans:wght@400;600;700&display=swap">
<style>
  :root {
    --brand-blue: #1f78c1;
    --ink: #111111;
    --card: #ffffff;
    --backdrop: #e9e9e9;
    --band-text: #ffffff;
  }
  * { margin: 0; padding: 0; box-sizing: border-box; }
  html, body { width: 1200px; height: 900px; overflow: hidden; }
  body {
    position: relative;
    background: var(--backdrop);
    font-family: "Open Sans", Arial, sans-serif;
    color: var(--ink);
  }
  .card {
    position: absolute;
    width: 594px;
    height: 383px;
    background: var(--card);
    overflow: hidden;
  }
  .card--front { left: 56px; top: 58px; }
  .card--back { left: 470px; top: 466px; }

  .side-band {
    position: absolute;
    top: 0; right: 0;
    width: 64px; height: 100%;
    background: var(--brand-blue);
  }
  .side-band__chevron { position: absolute; left: 0; width: 64px; height: 80px; }
  .card--front .side-band__chevron { top: 42px; }
  .card--back .side-band__chevron { top: 300px; }
  .side-band__url {
    position: absolute;
    left: 50%; top: 50%;
    transform: translate(-50%, -50%) rotate(-90deg);
    color: var(--band-text);
    font-size: 14px;
    letter-spacing: 0.3px;
    white-space: nowrap;
  }
  .card--back .side-band__url { top: 43%; }

  .brand { position: absolute; text-align: center; }
  .card--front .brand { left: 0; width: 523px; top: 114px; }
  .card--back .brand { left: 0; width: 530px; top: 208px; }
  .brand__name {
    font-weight: 700;
    font-size: 20px;
    letter-spacing: -0.3px;
    color: var(--ink);
  }
  .brand__slogan {
    margin-top: 2px;
    font-size: 17px;
    color: var(--brand-blue);
  }

  .contact { position: absolute; left: 44px; top: 198px; }
  .contact__name {
    font-weight: 700;
    font-size: 18px;
    color: var(--brand-blue);
    margin-left: 5px;
  }
  .contact__title {
    font-weight: 600;
    font-size: 14px;
    margin: 2px 0 0 5px;
  }
  .contact__list { list-style: none; margin-top: 16px; }
  .contact__item {
    display: flex;
    align-items: flex-start;
    font-size: 14px;
    line-height: 20px;
    margin-bottom: 4px;
  }
  .contact__icon {
    width: 14px; height: 14px;
    margin: 2px 8px 0 0;
    flex: none;
    fill: var(--brand-blue);
  }
</style>
</head>
<body>

  <section class="card card--front" aria-label="Card front">
    <div class="brand">
      <div class="brand__name">FERNDALE TIDEWELL PRESS</div>
      <div class="brand__slogan">Your information gateway</div>
    </div>

    <div class="contact">
      <div class="contact__name">OWEN MARSK</div>
      <div class="contact__title">Director of Sales &amp; Marketing</div>
      <ul class="contact__list">
        <li class="contact__item">
          <svg class="contact__icon" viewBox="0 0 14 14"><path d="M7 1 L13 7 H11 V13 H8.5 V9 H5.5 V13 H3 V7 H1 Z"/></svg>
          <span>#2817 - 562 E. Harlow Ave.<br>Vancouver, B.C. K7P2R4 Canada</span>
        </li>
        <li class="contact__item">
          <svg class="contact__icon" viewBox="0 0 14 14"><path d="M3 1 L5.5 1 L6.5 4.5 L5 5.8 C5.8 7.6 6.8 8.8 8.4 9.6 L9.6 8.2 L13 9.3 L13 11.8 C13 12.6 12.3 13.2 11.4 13 C6.2 12 2 7.8 1.1 2.6 C1 1.7 1.8 1 3 1 Z"/></svg>
          <span>555 014 3826</span>
        </li>
        <li class="contact__item">
          <svg class="contact__icon" viewBox="0 0 14 14"><path d="M1 3 H13 V11 H1 Z M1.8 3.6 L7 7.8 L12.2 3.6" stroke="#fff" stroke-width="0.9"/></svg>
          <span>owen@ferndaletidewell.biz</span>
        </li>
      </ul>
    </div>

    <div class="side-band">
      <svg class="side-band__chevron" viewBox="0 0 64 80" aria-hidden="true">
        <polyline points="64,4 4,40 64,76" fill="none" stroke="#fff" stroke-width="3"/>
      </svg>
      <span class="side-band__url">www.ferndaletidewell.biz</span>
    </div>
  </section>

  <section class="card card--back" aria-label="Card back">
    <div class="brand">
      <div class="brand__name">FERNDALE TIDEWELL PRESS</div>
      <div class="brand__slogan">Your information gateway</div>
    </div>

    <div class="side-band">
      <span class="side-band__url">www.ferndaletidewell.biz</span>
      <svg class="side-band__chevron" viewBox="0 0 64 80" aria-hidden="true">
        <polyline points="0,12 40,36 0,60" fill="none" stroke="#fff" stroke-width="3"/>
      </svg>
    </div>
  </section>

</body>
</html>
```